The RVH Relational Philanthropy Cycle

The title for this graphic is above. It must be included.
I am looking for a graphic representation of the relationship between the Christian school and the donor / pointing to the child (student) - the school's mission / outcome of investment through a gift / appreciation of the gift / communication of the gift impact for the child / stronger relationship going back to the child. This is not easy to do. I've tried to do it on my own and can't get it.
Any cliched child representations will be dismissed out of hand e.g. mortar boards, pencils, uniforms etc. The child should be abstract so that gender and race are irrelevant.
The key to this whole thing is the idea of RELATIONSHIP. The close relationship of donor and the Christian school, the pointing of that relationship to focus on the child / the school's mission, the outpouring of generosity that then happens in the heart of the donor and the gift that results, followed up by intentional work by the Christian school to thank and inform the donor - thank for the gift inform about the gift's expenditure and impact in the life of the child - all of which leads to a strengthening of the relationship and continued philanthropy as a never ending cycle.
It must be branded - logo and colors attached.
It must be obvious - easy to grasp the basic idea of relationship resulting in generosity / philanthropy. The visual should be clear - any words used illustrate - I should not 'need' the words to understand the idea.
I need it on a PP slide, jpeg, thumbnail. It must be highly legible in no more than 1/3 of a regular size piece of paper.
Our website is brightfieldacademyguild.org
google donor cultivation cycle or donor giving cycle to see many examples of cycles that are used in secular contexts - the big difference in RVH's is the focus on the child and the importance of the relationship.

```html
<!DOCTYPE html>
<html lang="en">
<head>
<meta charset="utf-8">
<title>The RVH Relational Philanthropy Cycle</title>
<link href="https://fonts.googleapis.com/css2?family=EB+Garamond:wght@400;500&display=swap" rel="stylesheet">
<style>
  :root {
    --brand-blue: #4677ac;
    --band-grey: #939393;
    --child-grey: #c8ced6;
    --arrow-grey: #c5ccd5;
    --coin-grey: #8f8f8f;
    --paper: #ffffff;
    --credit: #555555;
  }
  html, body {
    margin: 0;
    padding: 0;
    width: 1200px;
    height: 1177px;
    overflow: hidden;
    background: var(--paper);
  }
  .cycle-canvas {
    display: block;
    width: 1200px;
    height: 1177px;
  }
  .cycle-title {
    font-family: "EB Garamond", Georgia, serif;
    font-size: 36px;
    font-weight: 500;
    fill: var(--brand-blue);
    text-anchor: middle;
    letter-spacing: 0.5px;
  }
  .ring-label {
    font-family: "EB Garamond", Georgia, serif;
    font-size: 14px;
    fill: var(--paper);
    text-anchor: middle;
    letter-spacing: 0.3px;
  }
  .icon-credit {
    font-family: "EB Garamond", Georgia, serif;
    font-size: 7px;
    fill: var(--credit);
    text-anchor: middle;
  }
  .cycle-arrow {
    fill: none;
    stroke: var(--arrow-grey);
    stroke-width: 5;
  }
  .gift-arrow {
    fill: none;
    stroke: var(--arrow-grey);
    stroke-width: 3;
  }
  .ring-band { fill: none; stroke-width: 60; }
  .ring-blue { stroke: var(--brand-blue); }
  .ring-grey { stroke: var(--band-grey); }
  .ring-light { stroke: var(--child-grey); }
  .ring-core { fill: var(--paper); }
  .icon-fill { fill: var(--brand-blue); }
  .icon-limb { stroke: var(--brand-blue); stroke-width: 5; stroke-linecap: round; fill: none; }
  .icon-cutout { fill: var(--paper); }
  .heart { fill: var(--brand-blue); }
  .coin { fill: var(--coin-grey); }
  .coin-sign {
    font-family: Arial, Helvetica, sans-serif;
    font-size: 17px;
    font-weight: 700;
    fill: var(--paper);
    text-anchor: middle;
  }
</style>
</head>
<body>
<svg class="cycle-canvas" viewBox="0 0 1200 1177" xmlns="http://www.w3.org/2000/svg" aria-labelledby="cycle-heading">
  <defs>
    <marker id="arrowhead" viewBox="0 0 10 10" refX="5" refY="5" markerWidth="4" markerHeight="4" orient="auto-start-reverse">
      <path d="M0,0 L10,5 L0,10 Z" fill="#c5ccd5"/>
    </marker>
    <marker id="arrowhead-small" viewBox="0 0 10 10" refX="5" refY="5" markerWidth="5" markerHeight="5" orient="auto">
      <path d="M0,0 L10,5 L0,10 Z" fill="#c5ccd5"/>
    </marker>
    <path id="heart-shape" d="M0,4 C-3,-2 -12,-1 -10,6 C-9,10 -4,13 0,17 C4,13 9,10 10,6 C12,-1 3,-2 0,4 Z"/>
  </defs>

  <text id="cycle-heading" class="cycle-title" x="600" y="200">The RVH Relational Philanthropy Cycle</text>

  <g class="cycle-diagram" transform="translate(-13,8) scale(1.18)">

    <!-- Gift offering: coin in hand -->
    <g class="gift-hand">
      <circle class="coin" cx="532" cy="237" r="14"/>
      <text class="coin-sign" x="532" y="243">$</text>
      <rect class="icon-fill" x="492" y="256" width="10" height="16" rx="2"/>
      <path class="icon-fill" d="M504,258 L528,258 C534,258 534,264 528,264 L516,264 L540,264 L550,257 C554,255 557,259 553,262 L541,271 L504,271 Z"/>
    </g>

    <!-- Top cycle arrow: donor and school -->
    <path class="cycle-arrow" d="M408,322 Q520,250 632,322" marker-start="url(#arrowhead)" marker-end="url(#arrowhead)"/>

    <!-- Donor ring -->
    <g class="ring ring-donor">
      <circle class="ring-band ring-blue" cx="394" cy="470" r="88"/>
      <path class="ring-band ring-grey" d="M321.9,419.5 A88 88 0 0 1 466.1,419.5"/>
      <text class="ring-label" x="394" y="391">DONOR</text>
      <circle class="ring-core" cx="394" cy="470" r="58"/>
      <g class="donor-icon" role="img" aria-label="Donor: a person with a heart">
        <circle class="icon-fill" cx="394" cy="446" r="11"/>
        <path class="icon-fill" d="M372,504 L372,478 C372,466 382,461 394,461 C406,461 416,466 416,478 L416,504 Z"/>
        <use class="icon-cutout" href="#heart-shape" transform="translate(394,474) scale(0.75)"/>
      </g>
    </g>

    <!-- Christian school ring -->
    <g class="ring ring-school">
      <circle class="ring-band ring-blue" cx="645" cy="470" r="88"/>
      <path class="ring-band ring-grey" d="M572.9,419.5 A88 88 0 0 1 717.1,419.5"/>
      <text class="ring-label" x="647" y="384">CHRISTIAN</text>
      <text class="ring-label" x="647" y="399">SCHOOL</text>
      <circle class="ring-core" cx="645" cy="470" r="58"/>
      <g class="school-icon" role="img" aria-label="Christian school building with a cross">
        <rect class="icon-fill" x="643.5" y="430" width="3" height="14"/>
        <rect class="icon-fill" x="639" y="434" width="12" height="3"/>
        <path class="icon-fill" d="M645,443 L680,468 L675,468 L675,497 L615,497 L615,468 L610,468 Z"/>
        <rect class="ring-core" x="639" y="478" width="12" height="19" rx="6"/>
      </g>
    </g>

    <!-- Child ring -->
    <g class="ring ring-child">
      <circle class="ring-band ring-light" cx="520" cy="598" r="88"/>
      <path class="ring-band ring-blue" d="M582.2,660.2 A88 88 0 0 1 457.8,660.2"/>
      <text class="ring-label" x="520" y="692">CHILD</text>
      <circle class="ring-core" cx="520" cy="598" r="58"/>
      <g class="child-icon" role="img" aria-label="Two abstract children holding hands">
        <circle class="icon-fill" cx="504" cy="578" r="7"/>
        <path class="icon-fill" d="M498,588 L510,588 L516,612 L492,612 Z"/>
        <line class="icon-limb" x1="500" y1="612" x2="500" y2="628"/>
        <line class="icon-limb" x1="508" y1="612" x2="508" y2="628"/>
        <line class="icon-limb" x1="498" y1="592" x2="492" y2="606"/>
        <circle class="icon-fill" cx="538" cy="576" r="7"/>
        <rect class="icon-fill" x="531" y="586" width="14" height="26" rx="3"/>
        <line class="icon-limb" x1="534" y1="612" x2="534" y2="630"/>
        <line class="icon-limb" x1="542" y1="612" x2="542" y2="630"/>
        <line class="icon-limb" x1="544" y1="592" x2="550" y2="608"/>
        <path class="icon-limb" d="M510,592 L521,603 L532,592"/>
      </g>
    </g>

    <!-- Gift box pointing to the child -->
    <g class="gift-box">
      <rect class="icon-fill" x="486" y="318" width="68" height="14"/>
      <rect class="icon-fill" x="490" y="335" width="60" height="42"/>
      <rect class="icon-cutout" x="517" y="318" width="6" height="59"/>
      <path class="icon-fill" d="M520,316 C505,296 488,306 500,316 Z M520,316 C535,296 552,306 540,316 Z"/>
    </g>
    <path class="gift-arrow" d="M520,382 L520,560" marker-end="url(#arrowhead-small)"/>

    <!-- Bottom cycle arrow: relationship returns -->
    <path class="cycle-arrow" d="M354,622 C362,790 678,790 686,622" marker-start="url(#arrowhead)" marker-end="url(#arrowhead)"/>

    <!-- Outpouring of hearts -->
    <g class="hearts">
      <use class="heart" href="#heart-shape" transform="translate(436,703) scale(0.9)"/>
      <use class="heart" href="#heart-shape" transform="translate(470,724) scale(0.9)"/>
      <use class="heart" href="#heart-shape" transform="translate(520,728) scale(1.3)"/>
      <use class="heart" href="#heart-shape" transform="translate(568,724) scale(0.9)"/>
      <use class="heart" href="#heart-shape" transform="translate(603,703) scale(0.9)"/>
    </g>

    <text class="icon-credit" x="520" y="787">Icons by Iconmill from Glyphyard.com</text>
  </g>
</svg>
</body>
</html>
```